Flyer for the Radiant Harvest Worship Day 2020

I am looking to create a flyer for a one day prayer retreat our church is organizing.
This flyer will be posted on social media, websites and will also be printed so it can be mailed to people.
I am looking for something professional, with good use of our logo and band colors (logo colors).
I am counting on the designer's skill, creativity, art and knowledge of media communication to produce a flyer that will effectively and quickly convey the message we are trying to spread.
CONTENT OF THE FLYER:
Event title: Radiant Harvest Worship Day
Date: Tuesday July 2nd, 2020
Time: 11:00AM - 7:00PM
Belmora Hotel, 4876 Willowmere Street, Portland, Maine 04987 (Room: Evergrove)
Event Key words to highlight what the event is about: Prayer, Sharing the Word, Panel discussion, prophecy, Impartation.
Key phrases:
A one day prayer retreat.
Jesus Chris is Lord
Contact info:
www.toluvek.org
Phone: 207 555 0183
Email: contact@brightmeadowfold.org

```html
<!DOCTYPE html>
<html lang="en">
<head>
<meta charset="utf-8">
<title>Radiant Harvest Worship Day 2020</title>
<link href="https://fonts.googleapis.com/css2?family=Anton&family=Montserrat:wght@800&family=Tinos:wght@400;700&display=swap" rel="stylesheet">
<style>
  :root {
    --page: #ffffff;
    --ink: #13151d;
    --glow: #003a60;
    --blue: #3f8fb8;
    --orange: #f6961e;
    --white: #ffffff;
    --serif: "Tinos", "Times New Roman", serif;
    --display: "Anton", "Impact", sans-serif;
    --sans: "Montserrat", "Arial", sans-serif;
  }
  html, body {
    margin: 0;
    width: 1200px;
    height: 1000px;
    overflow: hidden;
    background: var(--page);
  }
  .flyer {
    position: absolute;
    left: 272px;
    top: 37px;
    width: 655px;
    height: 926px;
    background:
      radial-gradient(ellipse 300px 260px at 45% 60%, var(--glow) 0%, rgba(0,58,96,0.35) 55%, rgba(19,21,29,0) 100%),
      var(--ink);
    overflow: hidden;
    font-family: var(--serif);
  }
  .flyer > * { position: absolute; margin: 0; }

  .tagline {
    top: 26px; left: 79px;
    color: var(--blue);
    font-size: 22px;
    font-weight: 400;
    letter-spacing: 14px;
    white-space: nowrap;
  }

  .brand {
    top: 374px; left: 60px;
    display: flex; align-items: center; gap: 8px;
    color: var(--white);
    font-size: 30px;
    letter-spacing: 1px;
    line-height: 1;
  }
  .brand-dot {
    width: 12px; height: 12px; border-radius: 50%;
    background: var(--orange);
  }

  .headline {
    top: 0; left: 0;
    width: 100%; height: 100%;
    font-weight: normal;
    font-size: 16px;
  }
  .headline > span { position: absolute; white-space: nowrap; }

  .kicker {
    top: 432px;
    color: var(--blue);
    font-family: var(--sans);
    font-weight: 800;
    font-size: 19px;
    line-height: 1;
  }
  .kicker-left { left: 57px; letter-spacing: 14px; }
  .kicker-right { right: 38px; letter-spacing: 12px; }

  .title {
    top: 455px; left: 57px; width: 540px;
    display: flex; justify-content: space-between;
    color: var(--orange);
    font-family: var(--display);
    font-size: 104px;
    line-height: 1;
    text-shadow: 6px 8px 10px rgba(0,0,0,0.75);
  }

  .title-day {
    top: 550px; left: 450px;
    color: var(--blue);
    font-family: var(--sans);
    font-weight: 800;
    font-size: 40px;
    letter-spacing: 26px;
    line-height: 1;
  }

  .subtitle {
    top: 638px; left: 78px;
    color: var(--blue);
    font-size: 16px;
    letter-spacing: 11.4px;
    white-space: nowrap;
  }

  .date {
    top: 672px; left: 70px; width: 101px;
    text-align: right;
    line-height: 1;
  }
  .date-day { display: block; color: var(--orange); font-size: 15px; letter-spacing: 3px; }
  .date-month { display: block; color: var(--orange); font-size: 34px; letter-spacing: 4px; margin-top: 3px; }
  .date-num { display: block; color: var(--white); font-family: var(--display); font-size: 70px; letter-spacing: 4px; margin-top: 2px; line-height: 1; }
  .date-year { display: block; color: var(--white); font-size: 18px; letter-spacing: 10px; margin-top: 2px; }

  .box {
    top: 670px; height: 31px;
    border: 1.5px solid var(--blue);
    border-radius: 9px;
    box-sizing: border-box;
    color: var(--orange);
    font-family: var(--display);
    display: flex; align-items: center;
  }
  .box-time { left: 196px; width: 191px; justify-content: center; font-size: 23px; letter-spacing: 2px; }
  .box-time sup { font-family: var(--serif); font-size: 6px; letter-spacing: 0; margin: -10px 3px 0 1px; }
  .box-time .to { font-family: var(--serif); font-size: 12px; letter-spacing: 0; margin: 4px 4px 0 0; }
  .box-venue { left: 405px; width: 151px; padding-left: 8px; font-size: 23px; letter-spacing: 3px; }

  .program {
    top: 707px; left: 205px;
    padding: 0; list-style: none;
    color: var(--blue);
    font-size: 15px;
    line-height: 21.7px;
    letter-spacing: 0.6px;
    text-transform: uppercase;
  }

  .venue {
    top: 710px; left: 410px;
    color: var(--blue);
    font-size: 7.5px;
    letter-spacing: 3.2px;
    line-height: 15.5px;
    text-transform: uppercase;
    font-style: normal;
  }

  .call {
    top: 781px; left: 410px;
    color: var(--orange);
    line-height: 1;
  }
  .call-label { display: block; font-size: 11px; letter-spacing: 11px; }
  .call-number { display: block; font-size: 17px; letter-spacing: 3px; margin-top: 5px; }

  .contact {
    top: 866px; left: 0; width: 655px;
    text-align: center;
    color: var(--blue);
    font-weight: 700;
    font-size: 12px;
    letter-spacing: 6.5px;
    line-height: 21px;
  }
</style>
</head>
<body>
  <main class="flyer">
    <p class="tagline">JESUS CHRIS IS LORD</p>

    <div class="brand"><span class="brand-dot"></span>TOLUVEK</div>

    <h1 class="headline">
      <span class="kicker kicker-left">RADIANT</span>
      <span class="kicker kicker-right">HARVEST</span>
      <span class="title"><span>W</span><span>O</span><span>R</span><span>S</span><span>H</span><span>I</span><span>P</span></span>
      <span class="title-day">DAY</span>
    </h1>

    <p class="subtitle">A ONE DAY PRAYER RETREAT</p>

    <p class="date">
      <span class="date-day">TUS</span>
      <span class="date-month">JULY</span>
      <span class="date-num">02</span>
      <span class="date-year">2020</span>
    </p>

    <div class="box box-time">11:00<sup>AM</sup><span class="to">TO</span>7:00<sup>PM</sup></div>
    <div class="box box-venue">VENUE</div>

    <ul class="program">
      <li>Prayer</li>
      <li>Sharing the Word</li>
      <li>Panel Discussion</li>
      <li>Prophecy</li>
      <li>Impartation</li>
    </ul>

    <address class="venue">
      Belmora Hotel<br>
      4876 Willowmere Street<br>
      Portland, Maine 04987<br>
      (Room: Evergrove)
    </address>

    <p class="call">
      <span class="call-label">CALL US</span>
      <span class="call-number">207 555 0183</span>
    </p>

    <p class="contact">
      WWW.TOLUVEK.ORG<br>
      EMAIL: CONTACT@BRIGHTMEADOWFOLD.ORG
    </p>
  </main>
</body>
</html>
```